Training course diagram/design

A graphic/diagram for our website and brochures.

We are a training provider and run courses for people who wish to become professionally qualified clinical hypnotherapists.

The graphic needs to illustrate how our training course works at a glance. The training course is comprised of 5 x 4-day classroom based modules and one extra (6th) theory module which is distance learning. The diploma training is a 'rolling' course, so students can join at the beginning of any of the five (classroom) modules. It is important that it is clear from the image that there is not any specific order in which people must attend the modules (the modules have equal status). Attendance of all five modules (and completion of the theory module) will lead to the BQT (Brightmoor Trance Institute) Practitioner Diploma in Clinical Hypnotherapy Diploma.

The names of the classroom modules are:
Medical Hypnosis
Ericksonian Hypnosis
Hypno-psychotherapy
Solution Focused Hypnotherapy
Changework - NLP & Coaching

The 6th (theory module) is called:
The foundations of Hypnotherapy

I have uploaded our logo so you can see our colours/style. Our strapline is:
Practice-ready therapy training
Updates

Please use fonts used in the training school logo: 'Magmawave Caps Bold' and 'Avant Garde Bold'.

Target Market(s)

People who are wanting a creer change

Industry/Entity Type

Hypnotherapy

Font styles to use
Sans Serif
Other font styles liked:
• 'Magmawave Caps Bold' and 'Avant Garde Bold'.

Requirements
Must have
• an individual 'device' or symbol for each module (e.g. colour, shape, etc for each module) so that these can be used on different website pages or in literature where there might be a description of the contents of that module. Fonts that are consistent with branding and are easy to read.
Nice to have
• Something that complements or reflects the training school logo.

```html
<!DOCTYPE html>
<html lang="en">
<head>
<meta charset="utf-8">
<title>BQT Hypnotherapy Practitioner Diploma – Course Structure</title>
<link href="https://fonts.googleapis.com/css2?family=Poppins:wght@600;700&family=Questrial&display=swap" rel="stylesheet">
<style>
  :root {
    --bg: #ffffff;
    --foundation-ring: #45418c;
    --foundation-fin: #7a72b0;
    --classroom-ring: #c5c45e;
    --classroom-text: #0f5a4a;
    --diploma: #0f6654;
    --solution: #16205c;
    --ericksonian: #a51c2c;
    --psychotherapy: #234f58;
    --medical: #d84012;
    --changework: #66305f;
    --label: #ffffff;
  }
  html, body {
    margin: 0;
    padding: 0;
    width: 1200px;
    height: 846px;
    overflow: hidden;
    background: var(--bg);
  }
  .course-diagram {
    display: block;
    width: 1200px;
    height: 846px;
  }
  .foundation-ring { fill: none; stroke: var(--foundation-ring); stroke-width: 24; }
  .foundation-fin { fill: var(--foundation-fin); }
  .foundation-label {
    font-family: "Questrial", sans-serif;
    font-size: 19px;
    fill: var(--label);
    letter-spacing: 0.5px;
  }
  .classroom-ring { fill: none; stroke: var(--classroom-ring); stroke-width: 40; }
  .classroom-link { fill: var(--classroom-ring); }
  .classroom-label {
    font-family: "Poppins", sans-serif;
    font-weight: 600;
    font-size: 16px;
    fill: var(--classroom-text);
    letter-spacing: 0.4px;
  }
  .module-label {
    font-family: "Questrial", sans-serif;
    font-size: 19px;
    fill: var(--label);
    text-anchor: middle;
    font-weight: bold;
  }
  .diploma-label {
    font-family: "Poppins", sans-serif;
    font-weight: 700;
    font-size: 21px;
    fill: var(--label);
    text-anchor: middle;
  }
  .diploma { fill: var(--diploma); }
  .module-solution { fill: var(--solution); }
  .module-ericksonian { fill: var(--ericksonian); }
  .module-psychotherapy { fill: var(--psychotherapy); }
  .module-medical { fill: var(--medical); }
  .module-changework { fill: var(--changework); }
</style>
</head>
<body>
<svg class="course-diagram" viewBox="0 0 1500 1058" xmlns="http://www.w3.org/2000/svg" role="img" aria-label="BQT Hypnotherapy Practitioner Diploma: five 4-day classroom modules in a ring around the diploma, inside the distance learning module The foundations of Hypnotherapy">
  <defs>
    <path id="foundation-path" d="M750,1002 A474,474 0 1 1 750,54 A474,474 0 1 1 750,1002 A474,474 0 1 1 750,54 A474,474 0 1 1 750,1002"/>
    <path id="classroom-path" d="M750,184 A344,344 0 1 1 750,872 A344,344 0 1 1 750,184"/>
    <g id="fin">
      <path d="M478,150 Q466,205 512,216 Q500,168 548,112 Z"/>
    </g>
    <g id="link">
      <path d="M683,425 Q628,320 704,262 L730,270 Q670,322 683,425 Z"/>
    </g>
    <g id="link-band">
      <path d="M655,280 Q676,230 722,222 L728,256 Q702,258 688,288 Z"/>
    </g>
  </defs>

  <!-- Distance learning ring -->
  <g class="foundation">
    <g class="foundation-fin">
      <use href="#fin"/>
      <use href="#fin" transform="rotate(72 750 528)"/>
      <use href="#fin" transform="rotate(144 750 528)"/>
      <use href="#fin" transform="rotate(216 750 528)"/>
      <use href="#fin" transform="rotate(288 750 528)"/>
    </g>
    <circle class="foundation-ring" cx="750" cy="528" r="480"/>
    <text class="foundation-label" dy="0" text-anchor="middle">
      <textPath href="#foundation-path" startOffset="1489">The foundations of Hypnotherapy</textPath>
    </text>
    <text class="foundation-label" text-anchor="middle">
      <textPath href="#foundation-path" startOffset="2978">The foundations of Hypnotherapy</textPath>
    </text>
    <text class="foundation-label" text-anchor="middle">
      <textPath href="#foundation-path" startOffset="2233">DISTANCE LEANING MODULE</textPath>
    </text>
    <text class="foundation-label" text-anchor="middle">
      <textPath href="#foundation-path" startOffset="744">DISTANCE LEANING MODULE</textPath>
    </text>
  </g>

  <!-- Classroom ring -->
  <g class="classroom">
    <circle class="classroom-ring" cx="750" cy="528" r="354"/>
    <text class="classroom-label" text-anchor="middle"><textPath href="#classroom-path" startOffset="216">4 DAY CLASSROOM MODULES</textPath></text>
    <text class="classroom-label" text-anchor="middle"><textPath href="#classroom-path" startOffset="648">4 DAY CLASSROOM MODULES</textPath></text>
    <text class="classroom-label" text-anchor="middle"><textPath href="#classroom-path" startOffset="1080">4 DAY CLASSROOM MODULES</textPath></text>
    <text class="classroom-label" text-anchor="middle"><textPath href="#classroom-path" startOffset="1513">4 DAY CLASSROOM MODULES</textPath></text>
    <text class="classroom-label" text-anchor="middle"><textPath href="#classroom-path" startOffset="1945">4 DAY CLASSROOM MODULES</textPath></text>
  </g>

  <!-- Links from diploma to modules -->
  <g class="links">
    <g class="classroom-link">
      <use href="#link-band"/>
      <use href="#link-band" transform="rotate(72 750 528)"/>
      <use href="#link-band" transform="rotate(144 750 528)"/>
      <use href="#link-band" transform="rotate(216 750 528)"/>
      <use href="#link-band" transform="rotate(288 750 528)"/>
    </g>
    <use class="module-solution" href="#link"/>
    <use class="module-ericksonian" href="#link" transform="rotate(72 750 528)"/>
    <use class="module-psychotherapy" href="#link" transform="rotate(144 750 528)"/>
    <use class="module-medical" href="#link" transform="rotate(216 750 528)"/>
    <use class="module-changework" href="#link" transform="rotate(288 750 528)"/>
  </g>

  <!-- Modules -->
  <g class="module">
    <circle class="module-solution" cx="750" cy="172" r="74"/>
    <text class="module-label" x="750" y="152">Solution</text>
    <text class="module-label" x="750" y="176">Focused</text>
    <text class="module-label" x="750" y="200">Hypnotherapy</text>
  </g>
  <g class="module">
    <circle class="module-ericksonian" cx="1087" cy="418" r="74"/>
    <text class="module-label" x="1087" y="413">Ericksonian</text>
    <text class="module-label" x="1087" y="437">Hypnosis</text>
  </g>
  <g class="module">
    <circle class="module-psychotherapy" cx="958" cy="815" r="74"/>
    <text class="module-label" x="958" y="808">Hypno-</text>
    <text class="module-label" x="958" y="832">psychotherapy</text>
  </g>
  <g class="module">
    <circle class="module-medical" cx="541" cy="815" r="74"/>
    <text class="module-label" x="541" y="812">Medical</text>
    <text class="module-label" x="541" y="836">Hypnosis</text>
  </g>
  <g class="module">
    <circle class="module-changework" cx="413" cy="418" r="74"/>
    <text class="module-label" x="413" y="405">Changework -</text>
    <text class="module-label" x="413" y="429">NLP &amp;</text>
    <text class="module-label" x="413" y="453">Coaching</text>
  </g>

  <!-- Diploma -->
  <g class="diploma-hub">
    <circle class="diploma" cx="750" cy="528" r="124"/>
    <text class="diploma-label" x="750" y="490">BQT</text>
    <text class="diploma-label" x="750" y="517">Hypnotherapy</text>
    <text class="diploma-label" x="750" y="544">Practitioner</text>
    <text class="diploma-label" x="750" y="571">Diploma</text>
  </g>
</svg>
</body>
</html>
```